Mouse and Rodent Infestation Spray

Need to Design label for 16oz bottle. The image sent has our initial design on it. Need other options.

Industry/Entity Type

Pest Control

Colors

Designer to choose colors to be used in the design.

```html
<!DOCTYPE html>
<html lang="en">
<head>
<meta charset="utf-8">
<title>KLEARO Mouse &amp; Rat Infestation – 16 oz Label</title>
<link rel="stylesheet" href="https://fonts.googleapis.com/css2?family=Bebas+Neue&family=Exo+2:ital,wght@0,700;1,300;1,900&family=Roboto:wght@900&family=Roboto+Condensed:wght@700&display=swap">
<style>
  :root {
    --red: #ff0000;
    --black: #000000;
    --white: #ffffff;
    --green: #11bf11;
    --leaf-dark: #0a8c0a;
    --rat-grey: #6f6f6f;
    --badge-blue: #2c7fc4;
    --badge-green: #67b843;
    --page: #ffffff;
  }
  * { box-sizing: border-box; margin: 0; padding: 0; }
  html, body { width: 1200px; height: 1080px; overflow: hidden; background: var(--page); }

  .label {
    position: absolute; left: 238px; top: 47px;
    width: 724px; height: 986px;
    background: var(--black);
    border: 1px solid var(--black);
    overflow: hidden;
  }
  .label-header {
    position: absolute; left: 0; top: 0; width: 100%; height: 69px;
    background: var(--white);
    display: flex; align-items: center; justify-content: center; gap: 12px;
  }
  .brand-mark { width: 20px; height: 20px; border-radius: 50%; background: var(--black); }
  .brand-name {
    font-family: "Roboto", sans-serif; font-weight: 900;
    font-size: 36px; letter-spacing: 6px; color: var(--black);
  }
  .title-band {
    position: absolute; left: 0; top: 69px; width: 100%; height: 182px;
    background: var(--red);
  }
  .title-main {
    position: absolute; left: 0; top: 94px; width: 100%;
    text-align: center;
    font-family: "Bebas Neue", sans-serif; font-size: 124px; line-height: 1;
    color: var(--white); letter-spacing: 2px;
  }
  .title-sub {
    position: absolute; left: 0; top: 196px; width: 100%;
    text-align: center;
    font-family: "Exo 2", sans-serif; font-weight: 900; font-style: italic;
    font-size: 110px; line-height: 1; letter-spacing: -3px;
    color: var(--white);
    -webkit-text-stroke: 3px var(--red);
    paint-order: stroke fill;
  }
  .use-claim {
    position: absolute; left: 0; top: 318px; width: 100%;
    text-align: center;
    font-family: "Roboto", sans-serif; font-weight: 900;
    font-size: 36px; line-height: 42px; letter-spacing: 1px;
    color: var(--green);
  }
  .rat-art {
    position: absolute; left: 17px; top: 418px; width: 687px; height: 466px;
    background: radial-gradient(ellipse 60% 55% at 48% 45%, var(--rat-grey) 0%, var(--rat-grey) 55%, rgba(111,111,111,0) 100%);
    border-radius: 45% 50% 40% 35%;
  }
  .benefits {
    position: absolute; left: 162px; top: 470px; list-style: none;
  }
  .benefits li {
    display: flex; align-items: center; gap: 14px;
    font-family: "Exo 2", sans-serif; font-weight: 300; font-style: italic;
    font-size: 40px; line-height: 52px; color: var(--white);
  }
  .benefits li::before {
    content: ""; width: 24px; height: 21px; background: var(--white);
    clip-path: polygon(25% 0, 75% 0, 100% 50%, 75% 100%, 25% 100%, 0 50%);
  }
  .natural-leaf {
    position: absolute; left: 493px; top: 400px; width: 62px; height: 78px;
    background: linear-gradient(135deg, var(--green), var(--leaf-dark));
    border-radius: 0 70% 0 70%;
  }
  .natural-badge {
    position: absolute; left: 556px; top: 437px; width: 151px; height: 72px;
    border: 3px solid var(--green); border-radius: 10px;
    display: flex; flex-direction: column; align-items: center; justify-content: center;
    font-family: "Roboto", sans-serif; font-weight: 900;
    font-size: 25px; line-height: 27px; color: var(--green); text-align: center;
  }
  .cert-badge {
    position: absolute; left: 25px; top: 760px; width: 74px; height: 128px;
    background: linear-gradient(180deg, var(--badge-blue) 0 30%, var(--white) 30% 60%, var(--badge-green) 60%);
    border: 2px solid var(--badge-blue); border-radius: 12px 12px 8px 8px;
  }
  .formula {
    position: absolute; left: 155px; top: 786px; width: 440px;
    font-family: "Exo 2", sans-serif; font-weight: 700;
    font-size: 39px; line-height: 1; color: var(--red); letter-spacing: 1px;
  }
  .net-volume {
    position: absolute; right: 12px; top: 860px;
    font-family: "Roboto", sans-serif; font-weight: 900;
    font-size: 30px; line-height: 1; color: var(--white); white-space: nowrap;
  }
  .ingredients-band {
    position: absolute; left: 0; top: 894px; width: 100%; height: 92px;
    background: var(--red);
    display: flex; align-items: center; justify-content: center;
    font-family: "Roboto Condensed", sans-serif; font-weight: 700;
    font-size: 27px; color: var(--white); white-space: nowrap;
  }
</style>
</head>
<body>
  <main class="label">
    <header class="label-header">
      <span class="brand-name">KLEARO</span><span class="brand-mark"></span>
    </header>
    <div class="title-band"></div>
    <div class="rat-art" role="img" aria-label="Grey silhouette of a rat standing in profile with a long curling tail"></div>
    <h1 class="title-main">MOUSE &amp; RAT</h1>
    <h2 class="title-sub">Infestation</h2>
    <p class="use-claim">SAFE FOR INDOOR &amp;<br>OUTDOOR USE</p>
    <div class="natural-leaf" role="img" aria-label="Two green leaves"></div>
    <div class="natural-badge"><span>100%</span><span>NATURAL</span></div>
    <ul class="benefits">
      <li>Natural Bait</li>
      <li>Free of Pesticides</li>
      <li>Long-Lasting Control</li>
    </ul>
    <div class="cert-badge" role="img" aria-label="Safety certification badge"></div>
    <p class="formula">ADVANCED FORMULA</p>
    <p class="net-volume">16 OZ.</p>
    <footer class="ingredients-band">Active Ingredients : 48% Peppermint Oil , 52% Smart Ingredients</footer>
  </main>
</body>
</html>
```